Fernwick Digital Marketing Agency Website Design. I need a new website for my digital marketing agency. It needs to be FAST and easy to use. I want to be able to add videos to the main homepage like this page: https://www.lumatreeweb.example/search-marketing/cleveland-ohio-seo-companyI'd like to have the request quote tab on the top right side as well as my number above it. The following website is my favorite overall: http://www.vantorelgroup.example/ I'd love to copy something like that.

***** Website I want to copy: http://www.vantorelgroup.example/services/ ******
Updates

This needs to be a Wordpress website. Sorry for any confusion as this is the first time using MakerQuill. I need the homepage as described as well as a Services Page and Contact Us page. Services page should be simply yet creative with a spot for me to insert up to 8 services.

Target Market(s)

Business owners

Industry/Entity Type

Digital Marketing

Coding

Coded - Design and coding required

Number of Pages Required

3 page

Font styles to use
Other font styles liked:
• Oswald

Colors

Designer to choose colors to be used in the design.

Requirements
Must have
• I need to have a nice design/template to work off of in Wordpress. It needs to be bright and vibrant yet elegant in design.
Nice to have
• CTA at the top right as well as a place for the phone number. http://www.vantorelgroup.example/services/

```html
<!DOCTYPE html>
<html lang="en">
<head>
<meta charset="utf-8">
<title>Fernwick Digital Marketing Agency</title>
<link rel="stylesheet" href="https://fonts.googleapis.com/css2?family=Oswald:wght@400;500;600&family=Open+Sans:wght@400;600;700&display=swap">
<style>
:root{
  --red:#e3191f;
  --red-dark:#c11218;
  --blue:#1a6fe3;
  --blue-deep:#0d55c7;
  --navy:#1d2b4a;
  --ink:#1e1e1e;
  --text:#555a61;
  --muted:#8a8f96;
  --card:#f1f2f4;
  --line:#dfe2e6;
  --icon-line:#b8bec7;
  --white:#ffffff;
}
*{box-sizing:border-box;margin:0;padding:0}
html,body{width:1200px;height:5000px;overflow:hidden}
body{font-family:"Open Sans",Arial,sans-serif;color:var(--text);background:var(--white);position:relative}
h1,h2,h3,.btn,.nav a{font-family:"Oswald","Arial Narrow",sans-serif}
.btn{display:inline-block;padding:0 34px;height:58px;line-height:58px;color:var(--white);font-size:19px;text-transform:uppercase;letter-spacing:.5px;border-radius:4px;text-decoration:none}
.btn-red{background:var(--red)}
.btn-blue{background:var(--blue)}
section{position:relative;width:1200px}

/* hero */
.hero{height:660px;background:linear-gradient(90deg,#ffffff 0%,#f5f7fa 45%,#e6ebf1 100%)}
.hero-photo{position:absolute;right:0;top:0;width:620px;height:700px;background:linear-gradient(135deg,#dfe5ec 0%,#c9d3de 45%,#8ea7c6 100%)}
.topbar{position:absolute;top:30px;left:80px;right:80px;height:120px}
.brand{position:absolute;left:0;top:8px;display:flex;align-items:center;gap:14px}
.brand-dot{width:44px;height:44px;border-radius:50%;background:var(--red)}
.brand-name{font-family:"Oswald",sans-serif;font-weight:600;font-size:34px;color:var(--blue-deep)}
.call{position:absolute;right:186px;top:2px;font-family:"Oswald",sans-serif;font-size:22px;line-height:32px;color:var(--blue);font-weight:500;white-space:nowrap}
.call b{color:var(--red);font-weight:500}
.social-top{position:absolute;right:0;top:0;display:flex;gap:6px}
.social-top span{width:36px;height:36px;border:1px solid var(--icon-line);background:var(--white);position:relative}
.social-top span::after{content:"";position:absolute;left:14px;top:14px;width:6px;height:6px;border-radius:50%;background:var(--navy)}
.nav{position:absolute;right:0;top:62px;display:flex;align-items:center;gap:30px}
.nav a{font-size:15px;color:var(--ink);text-transform:uppercase;text-decoration:none;letter-spacing:.3px}
.nav a.cta{background:var(--red);color:var(--white);padding:0 16px;height:46px;line-height:46px;border-radius:3px}
.hero h1{position:absolute;left:80px;top:210px;font-size:56px;line-height:72px;font-weight:500;color:var(--ink);text-transform:uppercase}
.hero p{position:absolute;left:80px;top:368px;width:640px;font-size:19px;line-height:30px;color:#333}
.hero .actions{position:absolute;left:80px;top:496px;display:flex;gap:18px}

/* competitive banner */
.compete{height:330px}
.compete-box{position:absolute;left:80px;top:0;width:1040px;height:260px;border-radius:14px;background:linear-gradient(90deg,#f2f4f8 0%,#1a4f9d 42%,#0e2f66 100%);overflow:hidden}
.compete-docs{position:absolute;left:40px;top:30px;width:330px;height:210px;border-radius:6px;background:linear-gradient(135deg,#ffffff,#d7dde6)}
.compete h2{position:absolute;left:412px;top:38px;font-size:40px;color:var(--white);font-weight:400;white-space:nowrap}
.compete p{position:absolute;left:412px;top:106px;width:600px;font-size:17px;line-height:24px;color:#dfe7f5}
.compete .btn{position:absolute;left:412px;top:164px}

/* services */
.services{height:390px;display:flex;gap:26px;padding:0 80px}
.svc{flex:1;height:345px;background:var(--card);border-radius:6px;padding:34px 24px}
.svc svg{width:64px;height:64px;stroke:var(--blue);fill:none;stroke-width:3}
.svc h3{margin-top:20px;font-size:22px;font-weight:500;color:var(--ink);text-transform:uppercase}
.svc p{margin-top:12px;font-size:15px;line-height:24px}
.svc .more{display:block;margin-top:16px;font-size:13px;font-weight:700;color:var(--red);text-transform:uppercase}
.svc.active{background:var(--red)}
.svc.active svg{stroke:var(--white)}
.svc.active h3,.svc.active p,.svc.active .more{color:var(--white)}

/* video */
.video{height:640px;background:linear-gradient(135deg,#2a83f0 0%,var(--blue) 55%,#1460cf 100%)}
.video h2{position:absolute;top:52px;width:100%;text-align:center;font-size:40px;color:var(--white);font-weight:500;text-transform:uppercase}
.video-frame{position:absolute;left:275px;top:140px;width:650px;height:440px;border:10px solid var(--white);background:linear-gradient(135deg,#eef1f5 0%,#d8dde4 50%,#c7ccd3 100%)}
.play{position:absolute;left:50%;top:50%;width:96px;height:96px;margin:-48px 0 0 -48px;border-radius:50%;background:var(--white)}
.play svg{position:absolute;left:36px;top:30px}

/* b2b */
.b2b{height:650px}
.b2b-photo{position:absolute;left:80px;top:100px;width:495px;height:405px;background:linear-gradient(135deg,#e9edf2 0%,#b5bcc6 55%,#4c5564 100%)}
.b2b-copy{position:absolute;left:643px;top:90px;width:477px}
.b2b-copy h2{font-size:38px;line-height:48px;font-weight:500;color:var(--ink);text-transform:uppercase}
.b2b-copy p{margin-top:20px;font-size:15px;line-height:25px;color:var(--muted)}
.b2b-copy .btn{margin-top:30px}

/* resources */
.resources{height:660px;background:linear-gradient(135deg,#2b86f2 0%,var(--blue) 60%,#1762d2 100%)}
.resources h2{position:absolute;top:48px;width:100%;text-align:center;font-size:40px;color:var(--white);font-weight:500;text-transform:uppercase}
.res-grid{position:absolute;left:80px;top:130px;width:1040px;display:grid;grid-template-columns:repeat(4,1fr);gap:26px}
.res{height:236px;background:var(--white);border:2px solid var(--white)}
.res-cover{height:160px}
.res-foot{display:flex;justify-content:space-between;align-items:center;padding:0 12px;height:72px}
.res-foot span{font-family:"Oswald",sans-serif;font-size:22px;color:var(--ink)}
.res-foot svg{width:34px;height:30px}
.c1{background:linear-gradient(135deg,#2f7a7a,#d8dde2)}
.c2{background:linear-gradient(135deg,#d4e7f6,#3a8fd6)}
.c3{background:linear-gradient(135deg,#1c1c24,#c8232a)}
.c4{background:linear-gradient(135deg,#f3d13c,#f08ab0)}
.c5{background:linear-gradient(135deg,#e7ddc6,#8ab85c)}
.c6{background:linear-gradient(135deg,#6a1f6f,#e04a6a)}
.c7{background:linear-gradient(135deg,#eef0f3,#c8a98f)}
.c8{background:linear-gradient(135deg,#e8d8e8,#8b5aa5)}

/* proof */
.proof{height:390px}
.proof-copy{position:absolute;left:80px;top:60px;width:520px}
.proof-copy h2{font-size:38px;line-height:48px;font-weight:500;color:var(--ink);text-transform:uppercase}
.proof-copy p{margin-top:18px;font-size:15px;line-height:25px;color:var(--muted)}
.proof-copy .btn{margin-top:24px;height:54px;line-height:54px;font-family:"Open Sans",sans-serif;font-size:17px;text-transform:none;padding:0 22px}
.clients{position:absolute;left:650px;top:56px;width:470px;height:270px;display:grid;grid-template-columns:repeat(3,1fr)}
.client{display:flex;align-items:center;justify-content:center;border-right:1px solid var(--line);border-bottom:1px solid var(--line);font-family:"Oswald",sans-serif;font-size:24px;font-weight:600;color:#6b7078}
.client:nth-child(3n){border-right:none}
.client:nth-child(n+4){border-bottom:none}

/* grow cta */
.grow{height:480px;background:linear-gradient(90deg,#2a2e35 0%,#4a4f57 50%,#2d3138 100%)}
.grow-shade{position:absolute;inset:0;background:rgba(20,22,28,.45)}
.grow h2{position:absolute;top:76px;width:100%;text-align:center;font-size:48px;line-height:62px;font-weight:500;color:var(--white);text-transform:uppercase}
.grow .actions{position:absolute;top:306px;width:100%;display:flex;justify-content:center;gap:18px}

/* subscribe */
.subscribe{height:400px}
.sub-art{position:absolute;left:100px;top:40px;width:440px;height:320px;background:linear-gradient(135deg,#1f4c8c 0%,#6aa0d8 50%,#e6ecf4 100%)}
.sub-form{position:absolute;left:643px;top:50px;width:477px}
.sub-form h2{font-size:38px;font-weight:500;color:var(--ink);text-transform:uppercase}
.sub-form p{margin-top:16px;font-size:14px;line-height:23px;color:var(--muted)}
.fields{margin-top:26px;display:flex;gap:14px}
.field{flex:1;height:54px;border:1px solid var(--line);padding:0 14px;line-height:54px;font-size:14px;color:#a4a8ae}
.sub-form .btn{margin-top:16px;width:100%;text-align:center;font-size:22px}

/* footer */
.footer{height:340px;background:var(--blue)}
.social-foot{position:absolute;top:90px;width:100%;display:flex;justify-content:center;gap:22px}
.social-foot span{width:54px;height:54px;border:1px solid rgba(255,255,255,.7);position:relative}
.social-foot span::after{content:"";position:absolute;left:22px;top:22px;width:8px;height:8px;border-radius:50%;background:var(--white)}
.footer p{position:absolute;top:190px;width:100%;text-align:center;font-size:15px;line-height:26px;color:var(--white)}
.footer p u{font-weight:700}
.copyright{position:absolute;bottom:0;width:100%;height:64px;line-height:64px;text-align:center;font-size:13px;color:#d7e5fb;background:var(--blue-deep)}
</style>
</head>
<body>

<section class="hero">
  <div class="hero-photo" role="img" aria-label="Photo of a smiling man in a checked shirt, resting his chin on his hand, in a bright office"></div>
  <div class="topbar">
    <div class="brand"><span class="brand-dot"></span><span class="brand-name">Fernwick</span></div>
    <div class="call">CALL : <b>(100) 555-0142</b></div>
    <div class="social-top" aria-label="Social links"><span></span><span></span><span></span><span></span></div>
    <nav class="nav">
      <a href="#">Our Approach</a><a href="#">Services</a><a href="#">Case Studies</a><a href="#">Resources</a><a href="#">About Us</a><a href="#" class="cta">Let's Connect</a>
    </nav>
  </div>
  <h1>Digital Marketing Agency<br>Focused on Results</h1>
  <p>Lorem ipsum dolor sit amet, consectetur adipiscing elit, sed do eiusmod tempor incididunt ut labore et dolore magna aliqua. Ut enim ad minim veniam, quis nostrud exercitation ullamco laboris nisi ut.</p>
  <div class="actions"><a class="btn btn-red" href="#">Learn More</a><a class="btn btn-blue" href="#">Contact Us</a></div>
</section>

<section class="compete">
  <div class="compete-box">
    <div class="compete-docs" role="img" aria-label="Stack of printed report pages"></div>
    <h2>How Competitive Is Your Company Online?</h2>
    <p>Compare Your Company To Over 200 Surveyed Manufacturers In Corwin County</p>
    <a class="btn btn-red" href="#">Download Now</a>
  </div>
</section>

<section class="services">
  <div class="svc">
    <svg viewBox="0 0 64 64"><rect x="6" y="10" width="52" height="34" rx="2"/><path d="M24 54h16M32 44v10M16 34l10-10 8 6 12-12"/></svg>
    <h3>Marketing Strategy</h3>
    <p>With revenue growth at the forefront of our strategy, we work to align your digital strategy with your sales goals...</p>
    <span class="more">Learn More »</span>
  </div>
  <div class="svc">
    <svg viewBox="0 0 64 64"><rect x="6" y="8" width="34" height="24" rx="3"/><path d="M14 32v8l8-8"/><rect x="24" y="30" width="34" height="22" rx="3"/><path d="M50 52v8l-8-8M32 38h18M32 44h12"/></svg>
    <h3>Content Marketing</h3>
    <p>Grow your brand as a thought leader by delivering relevant information to your highly targeted audience.</p>
    <span class="more">Learn More »</span>
  </div>
  <div class="svc active">
    <svg viewBox="0 0 64 64"><rect x="12" y="4" width="40" height="54" rx="3"/><circle cx="30" cy="28" r="9"/><path d="M37 35l9 9"/></svg>
    <h3>Search Marketing</h3>
    <p>Organic traffic is the ultimate lead generation effort. We find keyword opportunities your competition is missing.</p>
    <span class="more">Learn More »</span>
  </div>
  <div class="svc">
    <svg viewBox="0 0 64 64"><rect x="4" y="8" width="56" height="40" rx="3"/><path d="M4 16h56M24 56h16M32 48v8M24 26l-6 6 6 6M40 26l6 6-6 6M34 24l-4 16"/></svg>
    <h3>Web Development</h3>
    <p>We turn your website into a lead generation machine with responsive websites and optimized conversion points.</p>
    <span class="more">Learn More »</span>
  </div>
</section>

<section class="video">
  <h2>Whatch Our Vedio</h2>
  <div class="video-frame" role="img" aria-label="Video preview with flat illustrations of people working on digital marketing tasks">
    <div class="play"><svg width="30" height="36" viewBox="0 0 30 36"><path d="M0 0l30 18L0 36z" fill="#e3191f"/></svg></div>
  </div>
</section>

<section class="b2b">
  <div class="b2b-photo" role="img" aria-label="Photo of two business colleagues standing together in an office"></div>
  <div class="b2b-copy">
    <h2>Growing B2B Companies Is<br>What We Do Best.</h2>
    <p>Clients choose Vantorel Group because we get real results – more leads and sales. After 20+ years in business, our success stems from understanding B2B industries and knowing how to connect with online audiences. We're committed to advancing your company's growth.</p>
    <p>From accounting and financial services to manufacturing companies, we captivate potential buyers and customers and get them to connect with our clients. You are innovators, engineers and problem solvers at heart. Your story is unique, and possibly decades old. But how convincing is your online brand? We will work with you to capitalize on your biggest asset – knowledge – to generate the right leads and new business.</p>
    <a class="btn btn-red" href="#">Contact Us Today!</a>
  </div>
</section>

<section class="resources">
  <h2>Featured Resources</h2>
  <div class="res-grid">
    <div class="res"><div class="res-cover c1" role="img" aria-label="Ebook cover mockup"></div><div class="res-foot"><span>Free Ebook</span><svg viewBox="0 0 34 30"><rect x="1" y="8" width="32" height="21" fill="#1a6fe3"/><path d="M1 8l16 12 16-12" stroke="#fff" stroke-width="2" fill="none"/><path d="M12 6l5-5 5 5M17 1v10" stroke="#1a6fe3" stroke-width="2" fill="none"/></svg></div></div>
    <div class="res"><div class="res-cover c2" role="img" aria-label="Brochure cover mockup"></div><div class="res-foot"><span>Free Ebook</span><svg viewBox="0 0 34 30"><rect x="1" y="8" width="32" height="21" fill="#1a6fe3"/><path d="M1 8l16 12 16-12" stroke="#fff" stroke-width="2" fill="none"/><path d="M12 6l5-5 5 5M17 1v10" stroke="#1a6fe3" stroke-width="2" fill="none"/></svg></div></div>
    <div class="res"><div class="res-cover c3" role="img" aria-label="Dark flyer cover mockup"></div><div class="res-foot"><span>Free Ebook</span><svg viewBox="0 0 34 30"><rect x="1" y="8" width="32" height="21" fill="#1a6fe3"/><path d="M1 8l16 12 16-12" stroke="#fff" stroke-width="2" fill="none"/><path d="M12 6l5-5 5 5M17 1v10" stroke="#1a6fe3" stroke-width="2" fill="none"/></svg></div></div>
    <div class="res"><div class="res-cover c4" role="img" aria-label="Colourful brochure mockup"></div><div class="res-foot"><span>Free Ebook</span><svg viewBox="0 0 34 30"><rect x="1" y="8" width="32" height="21" fill="#1a6fe3"/><path d="M1 8l16 12 16-12" stroke="#fff" stroke-width="2" fill="none"/><path d="M12 6l5-5 5 5M17 1v10" stroke="#1a6fe3" stroke-width="2" fill="none"/></svg></div></div>
    <div class="res"><div class="res-cover c5" role="img" aria-label="Product flyer mockup"></div><div class="res-foot"><span>Free Ebook</span><svg viewBox="0 0 34 30"><rect x="1" y="8" width="32" height="21" fill="#1a6fe3"/><path d="M1 8l16 12 16-12" stroke="#fff" stroke-width="2" fill="none"/><path d="M12 6l5-5 5 5M17 1v10" stroke="#1a6fe3" stroke-width="2" fill="none"/></svg></div></div>
    <div class="res"><div class="res-cover c6" role="img" aria-label="Event poster mockup"></div><div class="res-foot"><span>Free Ebook</span><svg viewBox="0 0 34 30"><rect x="1" y="8" width="32" height="21" fill="#1a6fe3"/><path d="M1 8l16 12 16-12" stroke="#fff" stroke-width="2" fill="none"/><path d="M12 6l5-5 5 5M17 1v10" stroke="#1a6fe3" stroke-width="2" fill="none"/></svg></div></div>
    <div class="res"><div class="res-cover c7" role="img" aria-label="Beauty brochure mockup"></div><div class="res-foot"><span>Free Ebook</span><svg viewBox="0 0 34 30"><rect x="1" y="8" width="32" height="21" fill="#1a6fe3"/><path d="M1 8l16 12 16-12" stroke="#fff" stroke-width="2" fill="none"/><path d="M12 6l5-5 5 5M17 1v10" stroke="#1a6fe3" stroke-width="2" fill="none"/></svg></div></div>
    <div class="res"><div class="res-cover c8" role="img" aria-label="Folded brochure mockup"></div><div class="res-foot"><span>Free Ebook</span><svg viewBox="0 0 34 30"><rect x="1" y="8" width="32" height="21" fill="#1a6fe3"/><path d="M1 8l16 12 16-12" stroke="#fff" stroke-width="2" fill="none"/><path d="M12 6l5-5 5 5M17 1v10" stroke="#1a6fe3" stroke-width="2" fill="none"/></svg></div></div>
  </div>
</section>

<section class="proof">
  <div class="proof-copy">
    <h2>The Proof Is in the Vantorel<br>Pudding</h2>
    <p>We love what we do. And we credit great clients for our happiness. They lean on us to shape creative content marketing strategies that involve everything from SEO and website design to email marketing and social media. We're passionate about the down and dirty work. The results are genuine fruits us.</p>
    <a class="btn btn-red" href="#">Learn more about the work we've done.</a>
  </div>
  <div class="clients">
    <div class="client">Calloway</div><div class="client">Marten</div><div class="client">Brightwell</div>
    <div class="client">Zephra</div><div class="client">Ostrand</div><div class="client">Hollin</div>
  </div>
</section>

<section class="grow" role="img" aria-label="Darkened photo of a business team meeting around a table">
  <div class="grow-shade"></div>
  <h2>Are You Ready to Grow Your<br>Company's Revenue With<br>Digital Marketing?</h2>
  <div class="actions"><a class="btn btn-red" href="#">See Results We've Produced</a><a class="btn btn-blue" href="#">Let's Chat</a></div>
</section>

<section class="subscribe">
  <div class="sub-art" role="img" aria-label="Stack of printed brochures and magazines"></div>
  <div class="sub-form">
    <h2>Subscribe to Happy Hour!</h2>
    <p>Subscribe to our newsletter to ensure that your company website is pulling in traffic. Learn about our staff, and to get random facts each month!</p>
    <div class="fields"><div class="field">Enter Email :</div><div class="field">Company Name :</div></div>
    <a class="btn btn-red" href="#">Sign Up!</a>
  </div>
</section>

<section class="footer">
  <div class="social-foot" aria-label="Social links"><span></span><span></span><span></span><span></span></div>
  <p>We shape digital marketing strategies for B2B and B2C businesses in <u>Ashdale, OH</u>, <u>Corwin, OH</u><br>and for clients located throughout the United States.</p>
  <div class="copyright">Copyright © FERNWICK DIGITAL MARKETING 2019 . All Right Reserved</div>
</section>

</body>
</html>
```